Bref créative
Brightwave IT Business cards
Professional
Kenneth Darrow
Chief Information Officer
248 Maple Hollow Rd
KDarrow@BrightwaveIT.example
www.brightwaveit.example
IT managed services
Managed backups
Web Hosting
Email Hosting
Spam Filtering
Networking
Structured Cabling
Project Planning
Colocation Services

```html
<!DOCTYPE html>
<html lang="en">
<head>
<meta charset="utf-8">
<title>Brightwave IT Business Cards</title>
<link href="https://fonts.googleapis.com/css2?family=Open+Sans:ital,wght@0,400;0,600;0,700;1,400;1,600&display=swap" rel="stylesheet">
<style>
  :root {
    --page-bg: #ffffff;
    --card-bg: #ffffff;
    --card-edge: #d4d6d9;
    --brand-blue: #1f6fc2;
    --accent-blue: #2b86d6;
    --text-dark: #3a3d42;
    --text-muted: #5f636a;
    --corner-light: #f2f3f5;
    --corner-dark: #b9bcc1;
    --divider: #9aa0a8;
  }
  * { box-sizing: border-box; margin: 0; padding: 0; }
  html, body {
    width: 1200px; height: 523px; overflow: hidden;
    background: var(--page-bg);
    font-family: "Open Sans", Arial, sans-serif;
  }
  .canvas { position: relative; width: 1200px; height: 523px; }
  .card {
    position: absolute; top: 101px; width: 548px; height: 321px;
    background: var(--card-bg);
    border: 1px solid var(--card-edge);
    overflow: hidden;
  }
  .card--front { left: 36px; }
  .card--back { left: 642px; }
  .card__corners { position: absolute; inset: 0; width: 100%; height: 100%; }

  .brand {
    position: absolute; left: 34px; top: 40px;
    display: flex; align-items: center; gap: 10px;
  }
  .brand__dot {
    width: 34px; height: 34px; border-radius: 50%;
    background: var(--brand-blue);
  }
  .brand__name {
    font-size: 34px; font-weight: 600; color: var(--brand-blue);
    letter-spacing: 0.5px; line-height: 1;
  }

  .person { position: absolute; left: 34px; top: 136px; }
  .person__name { font-size: 15px; font-weight: 700; color: var(--brand-blue); line-height: 18px; }
  .person__title { font-size: 12.5px; font-style: italic; font-weight: 600; color: var(--text-muted); line-height: 17px; }

  .contact {
    position: absolute; left: 34px; top: 206px;
    font-size: 11px; color: var(--text-dark); line-height: 14.5px;
    border-collapse: collapse;
  }
  .contact th { font-weight: 400; text-align: left; padding-right: 6px; white-space: nowrap; }
  .contact td { white-space: nowrap; }

  .divider {
    position: absolute; left: 355px; top: 164px; width: 1px; height: 118px;
    background: var(--divider);
  }

  .services {
    position: absolute; left: 367px; top: 166px; list-style: none;
    font-size: 11px; color: var(--brand-blue); line-height: 16.5px;
  }
  .services li { display: flex; align-items: center; gap: 4px; }
  .services li::before {
    content: ""; width: 7px; height: 7px; border-radius: 50%;
    background: var(--accent-blue); flex: none;
  }
</style>
</head>
<body>
<main class="canvas">
  <section class="card card--front" aria-label="Business card front">
    <svg class="card__corners" viewBox="0 0 548 321" aria-hidden="true">
      <defs>
        <linearGradient id="cornerShadeTop" x1="0" y1="0" x2="1" y2="1">
          <stop offset="0" stop-color="var(--corner-light)"/>
          <stop offset="1" stop-color="var(--corner-dark)"/>
        </linearGradient>
        <linearGradient id="cornerShadeBottom" x1="1" y1="0" x2="0" y2="1">
          <stop offset="0" stop-color="var(--corner-light)"/>
          <stop offset="1" stop-color="var(--corner-dark)"/>
        </linearGradient>
      </defs>
      <path d="M412 0 Q520 20 548 140 L548 0 Z" fill="url(#cornerShadeTop)"/>
      <path d="M405 0 Q522 16 548 150" fill="none" stroke="var(--accent-blue)" stroke-width="3"/>
      <path d="M0 232 Q20 305 148 321 L0 321 Z" fill="url(#cornerShadeBottom)"/>
      <path d="M0 224 Q14 308 156 321" fill="none" stroke="var(--accent-blue)" stroke-width="3"/>
    </svg>

    <div class="brand">
      <span class="brand__dot"></span>
      <span class="brand__name">Brightwave IT</span>
    </div>

    <div class="person">
      <p class="person__name">Kenneth Darrow</p>
      <p class="person__title">Chief Information Officer</p>
    </div>

    <table class="contact">
      <tr><th>Address</th><td>: 248 Maple Hollow Rd</td></tr>
      <tr><th>Phone</th><td>: 512-555-0147</td></tr>
      <tr><th>Email</th><td>: KDarrow@BrightwaveIT.example</td></tr>
      <tr><th>Website</th><td>: www.brightwaveit.example</td></tr>
    </table>

    <div class="divider"></div>

    <ul class="services">
      <li>IT managed services</li>
      <li>Managed backups</li>
      <li>Web Hosting</li>
      <li>Email Hosting</li>
      <li>Spam Filtering</li>
      <li>Colocation Services</li>
    </ul>
  </section>

  <section class="card card--back" aria-label="Business card back">
    <svg class="card__corners" viewBox="0 0 548 321" aria-hidden="true">
      <defs>
        <linearGradient id="backShadeTop" x1="0" y1="0" x2="1" y2="1">
          <stop offset="0" stop-color="var(--corner-light)"/>
          <stop offset="1" stop-color="var(--corner-dark)"/>
        </linearGradient>
        <linearGradient id="backShadeBottom" x1="1" y1="0" x2="0" y2="1">
          <stop offset="0" stop-color="var(--corner-light)"/>
          <stop offset="1" stop-color="var(--corner-dark)"/>
        </linearGradient>
      </defs>
      <path d="M410 0 Q528 24 548 165 L548 0 Z" fill="url(#backShadeTop)"/>
      <path d="M402 0 Q530 18 548 176" fill="none" stroke="var(--accent-blue)" stroke-width="3"/>
      <path d="M0 190 Q14 306 150 321 L0 321 Z" fill="url(#backShadeBottom)"/>
      <path d="M0 180 Q8 310 160 321" fill="none" stroke="var(--accent-blue)" stroke-width="3"/>
    </svg>
  </section>
</main>
</body>
</html>
```